Voltmark Advisory Grupe Stationary
business cards, letter head, envelopes, fax sheet and shipping label
Voltmark Advisory Grupe Stationary - Energy
Creative Brief
Professional
Tom Wellsby
Operations Manager
Voltmark Advisory Group C/o Miles R. Dunstan Esq., Coral Court and West Ridge Road P.O. Box K-57819
office - 242-555-0193
twellsby@voltmarkadvisorygroup.example
www.voltmarkadvisorygroup.example
USA Cel # 832-555-0146

```html
<!DOCTYPE html>
<html lang="en">
<head>
<meta charset="utf-8">
<title>Voltmark Advisory Group – Business Card</title>
<link href="https://fonts.googleapis.com/css2?family=Source+Sans+3:wght@400;600;700&display=swap" rel="stylesheet">
<style>
  :root {
    --page: #ffffff;
    --card: #ffffff;
    --card-edge: #d4d4d4;
    --ink: #1a1a1a;
    --brand: #1f5f9e;
    --blue-deep: #1a64a8;
    --blue-light: #4c9bd6;
    --gold: #f6b82e;
    --on-blue: #ffffff;
  }
  * { margin: 0; padding: 0; box-sizing: border-box; }
  html, body {
    width: 1200px; height: 744px; overflow: hidden;
    background: var(--page);
    font-family: "Source Sans 3", sans-serif;
  }
  .canvas { position: relative; width: 1200px; height: 744px; }
  .card {
    position: absolute; left: 100px; top: 112px;
    width: 1062px; height: 588px;
    background: var(--card);
    border: 1px solid var(--card-edge);
    box-shadow: 0 2px 6px rgba(0,0,0,0.12);
    overflow: hidden;
  }
  .card-wave { position: absolute; inset: 0; width: 100%; height: 100%; }
  .brand {
    position: absolute; left: 45px; top: 64px;
    display: flex; align-items: center; gap: 14px;
  }
  .brand-mark { width: 50px; height: 50px; background: var(--brand); }
  .brand-name {
    font-weight: 700; font-size: 34px; color: var(--brand);
    letter-spacing: 0.5px;
  }
  .person {
    position: absolute; right: 124px; top: 176px;
    text-align: right; color: var(--ink);
  }
  .person-name { font-size: 38px; font-weight: 400; line-height: 1.1; }
  .person-title { font-size: 23px; font-weight: 400; line-height: 1.2; margin-top: 2px; }
  .contact {
    position: absolute; left: 45px; top: 338px;
    color: var(--on-blue); font-size: 24px; line-height: 33.5px;
  }
</style>
</head>
<body>
<div class="canvas">
  <div class="card">
    <svg class="card-wave" viewBox="0 0 1062 588" preserveAspectRatio="none" aria-hidden="true">
      <defs>
        <linearGradient id="blueSweep" x1="0" y1="0" x2="1" y2="0.3">
          <stop offset="0" stop-color="var(--blue-deep)"/>
          <stop offset="1" stop-color="var(--blue-light)"/>
        </linearGradient>
      </defs>
      <path fill="url(#blueSweep)"
        d="M0,194 C160,202 360,262 500,300 C540,310 570,302 600,292 C640,280 680,280 720,280 L880,280 C940,282 960,312 990,352 C1020,397 1040,422 1062,437 L1062,588 L0,588 Z"/>
      <path fill="none" stroke="var(--gold)" stroke-width="9"
        d="M0,182 C160,190 360,250 500,288 C540,298 570,290 600,280 C640,268 680,268 720,268 L880,268 C940,270 960,300 990,340 C1020,385 1040,410 1062,425"/>
    </svg>

    <div class="brand">
      <span class="brand-mark"></span>
      <span class="brand-name">Voltmark Advisory Group</span>
    </div>

    <div class="person">
      <div class="person-name">Tom Wellsby</div>
      <div class="person-title">Operations Manager</div>
    </div>

    <div class="contact">
      <div>Voltmark Advisory Group, C/o Miles R. Dunstan Esq.,</div>
      <div>Coral Court and West Ridge Road, P.O. Box K-57819</div>
      <div>Phone: office - 242-555-0193 | Cell: 242-555-0178</div>
      <div>Email: twellsby@voltmarkadvisorygroup.example</div>
      <div>www.voltmarkadvisorygroup.example</div>
      <div>USA Cel # 832-555-0146</div>
    </div>
  </div>
</div>
</body>
</html>
```